Fun, challenging, and inspirational guide for life change - written by a coach, therapist and founde

I need (1) cover design for a book titled:
"THE WANDERER'S TOOLKIT FOR MIND-SHIFTING IDEAS" - the surprisingly practical magic of believing and taking action

A 2ND COVER will be need for a companion ebook, titled:
"THE HEARTH LEDGER FOR PURPOSE AND CONTENTMENT - 3 steps to help unlock and unleash the unlimited you by loving your limitations

These books will be used to promote a larger suite of products and services devoted to empowering and inspiring a community of OVERCOMERS.

For reference check out www.brightquillpath.com

I've included some photos for visual reference points.

DESIGNS CONCEPTS:
CLEAN - A BLEND OF PAST AND PRESENT - MODERN AND THE SACRED) (...The Marlowe's Atlas meets

Target Market(s)

young and aspiring professionals and seasoned pros looking for life-changes due to feeling unfulfilled in their profession and relationships

Industry/Entity Type

Life Coaching

Font styles to use
Serif
Sans Serif

Requirements
Must have
• CREATIVITY - ORIGINALITY - WICKEDLY CLEAN DESIGN- AND IMPACTFUL TRANSLATION OF BRAND CONCEPT - COLOR AND PUNCH
Nice to have
• I included some photos as reference point - **PLEASE SEE THE PHOTOS FOR THE STAR-GAZERS DESIGNS** - I really like the feeling they provoke - I want to give the viewer a sense of the journey that can be taken when they dive into these books.
• Basically, riff off the design profiles and colors included in the STAR-GAZER covers.
• MUSTS INCLUDE -
• -ORIGINALITY
• - IMPACT
• - COLOR
• - ORIGINAL DESIGNS+
• +
Should not have
• STAY AWAY FROM...
• 1 OVERUSED AND TRENDY ICONS
• - ESOTERIC IMAGES
• - FLOWERY SCRIPTS
• - I AM REALLY LOOKING FOR A UPDATE OF THE TYPICAL SELF-HELP BOOK COVERS WHICH RELY TOO MUCH ON FLOWERY AND SACRED IMAGERY
• THANK YOU - feel free to unleash your creativity!

```html
<!DOCTYPE html>
<html lang="en">
<head>
<meta charset="utf-8">
<title>The Hearth Ledger for Purpose and Contentment — Book Cover</title>
<link rel="stylesheet" href="https://fonts.googleapis.com/css2?family=Cinzel+Decorative:wght@400;700&family=Cinzel:wght@400&family=Cormorant+SC:wght@600&display=swap">
<style>
  :root {
    --bg-top: #3a2230;
    --bg-bottom: #5b2f3f;
    --ink: #fbf6f4;
    --ornament-light: #eee3e6;
    --ornament-deep: #b99aa5;
  }
  * { margin: 0; padding: 0; box-sizing: border-box; }
  html, body {
    width: 800px;
    height: 1200px;
    overflow: hidden;
    background: var(--bg-top);
  }
  .cover {
    position: relative;
    width: 800px;
    height: 1200px;
    background: linear-gradient(180deg, var(--bg-top) 0%, var(--bg-bottom) 100%);
    color: var(--ink);
    text-align: center;
    overflow: hidden;
  }
  .title {
    position: absolute;
    top: 40px;
    left: 0;
    width: 100%;
    font-family: "Cinzel Decorative", "Cinzel", serif;
    font-weight: 400;
    line-height: 1;
  }
  .title-lead {
    display: block;
    font-size: 102px;
    letter-spacing: 1px;
  }
  .title-main {
    display: block;
    font-size: 84px;
    margin-top: 14px;
  }
  .title-tail {
    display: block;
    font-size: 37px;
    margin-top: 22px;
  }
  .subtitle {
    position: absolute;
    top: 358px;
    left: 0;
    width: 100%;
    font-family: "Cormorant SC", serif;
    font-weight: 600;
    font-size: 21px;
    text-transform: uppercase;
    letter-spacing: 2px;
    line-height: 42px;
  }
  .ornament {
    position: absolute;
    left: 150px;
    top: 476px;
    width: 500px;
    height: 480px;
  }
  .author {
    position: absolute;
    top: 1042px;
    left: 0;
    width: 100%;
    font-family: "Cinzel", serif;
    font-weight: 400;
    font-size: 90px;
    line-height: 1;
    letter-spacing: 1px;
  }
</style>
</head>
<body>
  <main class="cover">
    <h1 class="title">
      <span class="title-lead">The Hearth</span>
      <span class="title-main">Ledger</span>
      <span class="title-tail">For Purpose And Contentment</span>
    </h1>
    <p class="subtitle">3 steps to help unlock and unleash<br>the unlimited you</p>
    <svg class="ornament" viewBox="0 0 500 480" role="img" aria-label="Round white mandala ornament with petal and dot patterns">
      <defs>
        <radialGradient id="ornament-fill" cx="50%" cy="50%" r="50%">
          <stop offset="0%" stop-color="var(--ornament-deep)"/>
          <stop offset="100%" stop-color="var(--ornament-light)"/>
        </radialGradient>
      </defs>
      <circle cx="250" cy="240" r="232" fill="url(#ornament-fill)"/>
    </svg>
    <p class="author">AUTHOR NAME</p>
  </main>
</body>
</html>
```